Web Design Project - Cosmetic Medispa

Our client's current website www.brightvellora.com.au needs a major overhaul. We need a template for the Home page and an Inner/procedure page.
Their main audience is women 25-55.
The website navigation is as per the attached Word document.
Scrolling animation needed in the header section (we will animate the photo), with the words “Vellora care you can rely on” neatly over the top of the image.
The footer of the website needs to contain links to all their procedures per the attached word document (see the bottom part of the document).
“Virtual Consultation” button/icon/banner needed on Home page.
"Vellora Answer Locator" button/icon/banner needed on Home page (this is a tool that lets visitors search for problems (e.g. wrinkles) and it provides a solution (e.g. 'botox').
Add a “Subscribe for Specials” box to all pages.
Colour scheme to be along the lines of that used in the attached Marnio images.
Home page must use the following images that are attached (flipped yellow bikini, sarong, and doctor).

```html
<!DOCTYPE html>
<html lang="en">
<head>
<meta charset="utf-8">
<title>Vellora Cosmetic Medicine – Home</title>
<link rel="stylesheet" href="https://fonts.googleapis.com/css2?family=Arimo:wght@400;700&display=swap">
<style>
:root{
  --gold-top:#e9b86e;
  --gold-bottom:#d9a455;
  --purple:#2c1853;
  --purple-deep:#1f1040;
  --nav-dark:#2a2a2a;
  --nav-active:#8f72b6;
  --green:#8cc63f;
  --olive:#8e9b3e;
  --link-blue:#4a9ad8;
  --sky:#36b0e3;
  --panel:#f6f6f6;
  --footer:#2c2542;
  --maroon:#6a3044;
  --orange-link:#eea45a;
  --text:#3a3a3a;
  --white:#ffffff;
}
*{box-sizing:border-box;margin:0;padding:0}
html,body{width:975px;height:1200px;overflow:hidden}
body{position:relative;font-family:"Arimo",Arial,sans-serif;color:var(--text);background:var(--gold-bottom)}
.abs{position:absolute}

/* header */
.site-header{left:0;top:0;width:975px;height:132px;background:linear-gradient(180deg,var(--gold-top),var(--gold-bottom))}
.brand{left:140px;top:28px;width:110px;text-align:center;color:var(--white)}
.brand-mark{width:46px;height:46px;border-radius:50%;background:var(--white);margin:0 auto 6px}
.brand-name{font-size:17px;letter-spacing:2px;line-height:1}
.brand-sub{font-size:7px;letter-spacing:2px;margin-top:2px}
.call-now{left:369px;top:23px;font-size:14px;color:#5a4b3b}
.newsletter-link{left:369px;top:40px;font-size:10.5px;color:#111}
.partner-badge{left:574px;top:24px;width:142px;height:30px;background:#fbf7f0;border:1px solid #caa}
.welcome-video{left:718px;top:24px;width:124px;height:30px;background:#f7e54a;font-size:9px;font-weight:700;color:#2d3a8a;padding:5px 6px;line-height:1.1}
.welcome-video .photo{position:absolute;right:2px;top:2px;width:26px;height:26px;background:linear-gradient(#f2d2b0,#d9a27a)}
.tagline{left:298px;top:87px;font-size:14px;color:var(--white)}
.subscribe-box{left:653px;top:84px;width:148px;height:25px;border-radius:5px;background:#fff6ea;border:1px solid #c4956a;font-size:12px;color:#e0502e;padding:4px 8px}
.subscribe-go{left:805px;top:82px;width:27px;height:27px;border-radius:50%;background:#2a2a2a;border:2px solid #777;color:var(--white);font-size:11px;text-align:center;line-height:23px}

/* purple stage */
.stage{left:0;top:132px;width:975px;height:288px;background:linear-gradient(180deg,var(--purple-deep),var(--purple))}
.main-nav{left:127px;top:115px;width:720px;height:38px;background:linear-gradient(180deg,#4a4a4a,var(--nav-dark));font-size:11px;color:var(--white)}
.main-nav span{position:absolute;top:0;line-height:38px}
.main-nav .active{left:0;width:54px;height:38px;background:var(--nav-active);text-align:center}
.shop-link{left:696px;top:122px;display:flex;align-items:center;gap:6px;color:var(--sky);font-size:11px}
.cart-icon{width:25px;height:25px;border-radius:50%;background:var(--sky);border:2px solid #bfe6f6}
.hero{left:127px;top:167px;width:721px;height:237px;border:2px solid #bdb7cf;background:#fff;overflow:hidden}
.hero-beach{left:0;top:0;width:473px;height:233px;background:linear-gradient(180deg,#6aa6dc,#3f86c4)}
.hero-bikini{left:474px;top:0;width:114px;height:233px;background:linear-gradient(180deg,#c9b08a,#d8aa80)}
.hero-doctor{left:589px;top:0;width:128px;height:233px;background:linear-gradient(180deg,#4e86b8,#7fb0da)}
.hero-title{left:129px;top:142px;font-size:26px;line-height:27px;color:var(--white)}
.hero-dots{left:24px;top:208px;display:flex;gap:12px}
.hero-dots span{width:15px;height:15px;border-radius:50%;background:#3a4a22;border:2px solid var(--green)}
.hero-dots span.on{background:#333;border-color:#ddd}
.divider{left:0;top:420px;width:975px;height:3px;background:var(--olive)}

/* body copy */
.content-bg{left:0;top:423px;width:975px;height:498px;background:linear-gradient(180deg,#d9b57d,#c9a46c 40%,#dcb979 70%,#c59c62)}
.intro{left:126px;top:444px;width:705px;font-size:8.9px;line-height:10.4px;color:#333}
.intro p{margin-bottom:10.4px}

/* panel */
.panel{left:122px;top:621px;width:719px;height:291px;background:var(--panel)}
.section-title{font-size:13.5px;color:var(--green);line-height:14px}
.consult-form{left:17px;top:8px;width:158px}
.field{display:block;width:141px;height:15px;border:1px solid #3b6d6b;background:#fff;font-size:9.5px;padding:1px 3px;color:#234;margin-bottom:2px}
.form-label{font-size:9px;color:#3b6d6b;margin-top:7px}
.select{width:135px;height:14px;border:1px solid #777;font-size:9px;padding:0 3px;background:#fff;position:relative}
.select::after{content:"";position:absolute;right:0;top:0;width:11px;height:12px;background:#ddd;border-left:1px solid #999}
.textarea{width:140px;height:42px;border:1px solid #3b6d6b;background:#fff}
.captcha{width:130px;height:28px;background:#3aa9e8;color:var(--white);font-size:15px;letter-spacing:9px;font-weight:700;padding:5px 10px}
.captcha-input{width:132px;height:15px;border:1px solid #777;background:#fff;margin-top:2px}
.submit{left:38px;top:266px;width:92px;height:22px;border-radius:6px;background:linear-gradient(#4cb0f2,#1d79c8);color:var(--white);font-size:11px;text-align:center;line-height:22px}
.proc-image{left:218px;top:40px;width:245px;height:86px;border:1px solid #222;background:linear-gradient(90deg,#e0c2aa,#f0ebe2 55%,#b6d28a)}
.proc-list{left:236px;top:132px;font-size:8.6px;line-height:10.4px;color:var(--link-blue);list-style:none}
.read-more{left:387px;top:206px;font-size:9px;font-weight:700;color:#111}
.three-d{left:522px;top:20px}
.three-d-image{left:518px;top:46px;width:154px;height:123px;background:linear-gradient(135deg,#eef3f8,#d8c0a6)}
.three-d-rule{left:485px;top:178px;width:222px;height:1px;background:#ddd}
.three-d-link{left:537px;top:191px;font-size:10.5px;line-height:13px;color:var(--link-blue)}
.cta-frame{left:197px;top:225px;width:457px;height:59px;border:1px solid #a8a8a8;border-radius:4px;background:#e9e9e9}
.cta{position:absolute;top:6px;height:45px;font-size:13px;display:flex;align-items:center;gap:10px;padding-left:10px}
.cta .icon{width:44px;height:30px}
.cta-consult{left:5px;width:200px;background:linear-gradient(#f46ac0,#e0238e);color:#111}
.cta-consult .icon{background:#b01b6f}
.cta-finder{left:228px;width:223px;background:linear-gradient(#fbac46,#f18a12);color:var(--white)}
.cta-finder .icon{background:#2d4d8c}

/* footer */
.site-footer{left:0;top:921px;width:975px;height:210px;background:var(--footer)}
.treat-badge{left:138px;top:20px;width:72px;height:24px;background:#f0d631;border:1px solid #b59a10}
.foot-col{top:18px;font-size:8px;line-height:13.6px;color:var(--white)}
.foot-col h4{font-size:12px;font-weight:400;color:var(--green);margin-bottom:5px}
.foot-brand{left:110px;top:114px;width:102px;text-align:center;color:#b9b4c2}
.foot-brand .brand-mark{background:#b9b4c2;width:40px;height:40px}
.gallery-strip{left:238px;top:153px;width:555px;height:39px;border:2px solid #f0d631;background:linear-gradient(90deg,#e0b49a,#f0d8c8,#d8b8b0,#e8d0c0,#c8a890,#d8c8a0,#f0d080)}

.base{left:0;top:1131px;width:975px;height:69px;background:linear-gradient(180deg,#7a3a4e,var(--maroon))}
.base-links{left:117px;top:17px;font-size:8px;color:var(--white)}
.copyright{left:596px;top:13px;font-size:8px;color:var(--white)}
.social-bar{left:577px;top:27px;width:256px;height:34px;background:var(--white);border-radius:6px;display:flex;align-items:center;gap:5px;padding-left:8px}
.social-bar span{width:20px;height:20px;border-radius:4px;background:#8a8a8a}
.x18{left:845px;top:41px;font-size:10px;color:var(--white)}
.base-nav{left:118px;top:48px;font-size:10.5px;color:var(--orange-link)}
.base-nav span{position:absolute;top:0;white-space:nowrap}
</style>
</head>
<body>

<header class="abs site-header">
  <div class="abs brand"><div class="brand-mark"></div><div class="brand-name">VELLORA</div><div class="brand-sub">COSMETIC MEDICINE</div></div>
  <div class="abs call-now">Call Now: (08) 5550 1234</div>
  <div class="abs newsletter-link">Click here to Subscribe to Our Newsletter</div>
  <div class="abs partner-badge" role="img" aria-label="Radio partner badge"></div>
  <div class="abs welcome-video">Welcome Video<br><span style="font-size:7px">from Nurse Marlene</span><div class="photo" role="img" aria-label="Nurse portrait"></div></div>
  <div class="abs tagline">Vellora care you can rely on</div>
  <div class="abs subscribe-box">Subscribe for Specials</div>
  <div class="abs subscribe-go">go</div>
</header>

<section class="abs stage">
  <nav class="abs main-nav" style="top:-17px">
    <span class="active">Home</span><span style="left:63px">About</span><span style="left:108px">Procedures</span><span style="left:180px">Specials</span><span style="left:231px">Shop</span><span style="left:270px">Media</span><span style="left:312px">Contact</span>
  </nav>
  <div class="abs shop-link" style="top:-10px"><span class="cart-icon"></span>Our Online shop</div>
  <div class="abs hero" style="top:35px">
    <div class="abs hero-beach" role="img" aria-label="Woman in a sarong on a beach"></div>
    <div class="abs hero-bikini" role="img" aria-label="Torso in a yellow bikini"></div>
    <div class="abs hero-doctor" role="img" aria-label="Surgeon in mask and cap"></div>
    <div class="abs hero-title">Plastic Surgery Perth -<br>Cosmetic Surgery Perth WA</div>
    <div class="abs hero-dots"><span></span><span></span><span></span><span></span><span class="on"></span></div>
    <svg class="abs" style="left:461px;top:198px" width="12" height="24"><polygon points="12,0 12,24 0,12" fill="#8cc63f"/></svg>
    <svg class="abs" style="left:576px;top:198px" width="12" height="24"><polygon points="12,0 12,24 0,12" fill="#222"/></svg>
    <svg class="abs" style="left:705px;top:198px" width="12" height="24"><polygon points="12,0 12,24 0,12" fill="#222"/></svg>
  </div>
</section>
<div class="abs divider"></div>

<main>
  <div class="abs content-bg"></div>
  <div class="abs intro">
    <p>Plastic surgery, cosmetic surgery, dermal fillers, PRP (Dracula therapy or CGF) , btox, breast implants, liposuction, wrinkle treatments, IPL, laser hair removal, wrinkle relaxers, facelifts, eyelid surgery, laser surgery and other treatments as shown below are available in Perth, West Perth, Nedlands, Dalkeith, Subiaco, Cottesloe, Swanbourne, Mosman Park, Peppermint Grove, Joondalup, Applecross, Mandurah, Bunbury, Dunsborough, Karratha, Broome, Geraldton and Kalgoorlie.</p>
    <p>Dont go overseas to Thailand or Asia for your cosmetic surgery, risking the the third world problems and the risk of travel after surgery. If you cant drink the water why would you have your surgery there. See latest news for a horror story.</p>
    <p>Save on all your favourite cosmetic treatments. Call the clinic now on 5550 1234 to find out about our October special offers.</p>
    <p>Also ring now on 55507788 for an appointment in our new Applecross Clinic !</p>
    <p>*Not all services offered at all locations. Contact the clinic for more information.</p>
    <p>We aim to provide natural, subtle results from minimally invasive procedures.It is your face and body, only trust the experts. Full time and only practising in cosmetic plastic surgery. One of the first full time clinics in Australia with international recognition and featuring Dr Halden who is a Past Cosmetic President.</p>
  </div>

  <section class="abs panel">
    <form class="abs consult-form">
      <div class="section-title">Book a FREE 30<br>Minute Consultation</div>
      <div style="margin-top:7px"><span class="field">Name</span><span class="field">Email Address</span><span class="field">Phone</span></div>
      <div class="form-label">I would like more information on:</div>
      <div class="select">-- Please select --</div>
      <div class="form-label" style="margin-top:2px">Comments</div>
      <div class="textarea"></div>
      <div class="form-label" style="margin-top:10px">Enter Word Verification in box below<br>=</div>
      <div class="captcha">xyhqes</div>
      <div class="captcha-input"></div>
    </form>
    <div class="abs submit">SUBMIT</div>

    <div class="abs section-title" style="left:250px;top:19px">Our Procedures</div>
    <div class="abs proc-image" role="img" aria-label="Women enjoying skin treatments"></div>
    <ul class="abs proc-list">
      <li>» Liposuction</li><li>» Breast Implants</li><li>» Face Lift</li><li>» Intense Pulsed Light (IPL)</li><li>» Wrinkle Fillers</li><li>» Wrinkle Relaxers</li><li>» Thread Lift</li><li>» Cosmetic Surgery Procedures</li>
    </ul>
    <div class="abs read-more">Read More »</div>

    <div class="abs three-d section-title">NEW - 3D Procedures</div>
    <div class="abs three-d-image" role="img" aria-label="3D procedure viewer preview"></div>
    <div class="abs three-d-rule"></div>
    <div class="abs three-d-link">View your procedure in 3D<br>» Click Here</div>

    <div class="abs cta-frame">
      <div class="cta cta-consult"><span class="icon"></span>Virtual Consultation</div>
      <div class="cta cta-finder"><span class="icon"></span>Vellora Answer Locator</div>
    </div>
  </section>
</main>

<footer class="abs site-footer">
  <div class="abs treat-badge"></div>
  <div class="abs foot-col" style="left:238px"><h4>Breast</h4>Breast Implants<br>Breast Augmentation<br>Free Consultation</div>
  <div class="abs foot-col" style="left:353px"><h4>Body</h4>Liposuction<br>Liposculpture<br>Liposdissolve<br>CryoShape<br>Hair Removal<br>Fat Transfer<br>Mesotherapy</div>
  <div class="abs foot-col" style="left:433px"><h4>Face</h4>Dermal Fillers<br>Wrinkle Relaxers<br>Skin Rejuvenation<br>Thread Lift<br>Chemical Peels<br>Laser Resurfacing<br>Skin Polishing</div>
  <div class="abs foot-col" style="left:523px"><h4>Male</h4>Male Breast Reduction<br>Dermal Fillers<br>Wrinkle Relaxers<br>Skin Rolling<br>Eyelid Surgery<br>Liposculpture<br>CryoShape</div>
  <div class="abs foot-col" style="left:631px"><h4>About</h4>Nedlands Practice<br>Applecross Practice<br>The Medispa<br>Dr Halden<br>Nurse Marlene<br>Nursing Staff<br>Reception Staff</div>
  <div class="abs foot-col" style="left:749px"><h4>Home</h4>Specials<br>Virtual Consult<br>Shop<br>Media<br>FAQ<br>Blog<br>Contact Us</div>
  <div class="abs foot-brand"><div class="brand-mark"></div><div class="brand-name">VELLORA</div><div class="brand-sub">COSMETIC MEDICINE</div></div>
  <div class="abs gallery-strip" role="img" aria-label="Strip of treatment photos"></div>
</footer>

<div class="abs base">
  <div class="abs base-links">Privacy Policy | Site Map | Links | Related Websites</div>
  <div class="abs copyright">2012 Vellora Cosmetic Medicine. All Rights Reserved</div>
  <div class="abs social-bar">
    <span></span><span></span><span></span><span></span><span></span><span></span><span></span><span></span><span></span><span></span>
  </div>
  <div class="abs x18">X18</div>
  <nav class="abs base-nav"><span style="left:0">Home</span><span style="left:48px">About</span><span style="left:93px">Procedures</span><span style="left:165px">Specials</span><span style="left:217px">Shop</span><span style="left:255px">Media</span><span style="left:297px">Contact</span></nav>
</div>

</body>
</html>
```